Business Card for Bright Lantern

Please design a Modern Business card for a Online Marketing Company

Website: http://www.brightlantern-example.com.au

Please do NOT include physical address in design.

Industry/Entity Type

Business

```html
<!DOCTYPE html>
<html lang="en">
<head>
<meta charset="utf-8">
<title>Bright Lantern – Business Card</title>
<link rel="stylesheet" href="https://fonts.googleapis.com/css2?family=Roboto:wght@400;700;900&family=Roboto+Condensed:wght@400;700&display=swap">
<style>
  :root {
    --backdrop: #6e6e6e;
    --card: #ffffff;
    --brand-red: #b3222d;
    --accent-red: #e8493a;
    --accent-orange: #f0a02e;
    --ink: #111111;
    --rule: #f6c9a6;
  }
  * { box-sizing: border-box; margin: 0; padding: 0; }
  html, body {
    width: 983px; height: 1200px; overflow: hidden;
    background: var(--backdrop);
  }
  .stage { position: relative; width: 983px; height: 1200px; }
  .card {
    position: absolute; left: 31px; width: 924px; height: 560px;
    background: var(--card); overflow: hidden;
    box-shadow: 0 2px 6px rgba(0,0,0,0.25);
  }
  .card--front { top: 30px; }
  .card--back { top: 618px; }

  /* Front */
  .brand-mark {
    position: absolute; left: 140px; top: 200px; width: 88px; height: 88px;
    background: var(--brand-red);
  }
  .brand-name {
    position: absolute; left: 304px; top: 194px; line-height: 1.15;
    font-family: "Roboto", sans-serif; font-weight: 900; font-size: 56px;
    color: var(--brand-red); letter-spacing: 0.5px; white-space: nowrap;
  }
  .tagline {
    position: absolute; left: 412px; top: 254px; line-height: 1.15;
    font-family: "Roboto", sans-serif; font-weight: 700; font-size: 27px;
    color: var(--ink); white-space: nowrap;
  }
  .front-rule {
    position: absolute; left: 52px; right: 52px; top: 452px;
    height: 2px; background: var(--rule);
  }
  .front-contacts {
    position: absolute; left: 52px; right: 52px; top: 478px;
    display: flex; justify-content: space-between;
    font-family: "Roboto Condensed", sans-serif; font-size: 20px;
    color: var(--accent-red);
  }

  /* Back */
  .decor { position: absolute; }
  .decor--top {
    right: 0; top: 0; width: 420px; height: 300px;
    background: linear-gradient(225deg, rgba(179,34,45,0.45), rgba(240,160,46,0.2) 75%, rgba(240,160,46,0));
  }
  .decor--bottom {
    left: 0; bottom: 0; width: 300px; height: 230px;
    background: linear-gradient(45deg, rgba(179,34,45,0.45), rgba(240,160,46,0.2) 75%, rgba(240,160,46,0));
  }
  .person-name {
    position: absolute; left: 77px; top: 164px; line-height: 1.15;
    font-family: "Roboto Condensed", sans-serif; font-weight: 400; font-size: 78px;
    color: var(--accent-red); white-space: nowrap;
  }
  .person-role {
    position: absolute; left: 245px; top: 252px; line-height: 1.15;
    font-family: "Roboto Condensed", sans-serif; font-weight: 700; font-size: 24px;
    color: var(--accent-red); white-space: nowrap;
  }
  .contact-list {
    position: absolute; left: 377px; top: 336px; list-style: none;
    font-family: "Roboto Condensed", sans-serif; font-size: 32px; color: var(--ink);
  }
  .contact-list li { display: flex; height: 43px; line-height: 43px; white-space: nowrap; }
  .contact-key { width: 46px; color: var(--accent-orange); }
</style>
</head>
<body>
<div class="stage">
  <section class="card card--front">
    <div class="brand-mark"></div>
    <div class="brand-name">BRIGHT LANTERN</div>
    <div class="tagline">Shine online - Grow online</div>
    <div class="front-rule"></div>
    <div class="front-contacts">
      <span>plan@brightlantern-example.com.au</span>
      <span>0400 123 456</span>
      <span>brightlantern-example.com.au</span>
    </div>
  </section>

  <section class="card card--back">
    <div class="decor decor--top" role="img" aria-label="Decorative overlapping squares in red and orange"></div>
    <div class="decor decor--bottom" role="img" aria-label="Decorative overlapping squares in red and orange"></div>
    <div class="person-name">John Doe</div>
    <div class="person-role">Position Title</div>
    <ul class="contact-list">
      <li><span class="contact-key">M</span><span>plan@brightlantern-example.com.au</span></li>
      <li><span class="contact-key">W</span><span>brightlantern-example.com.au</span></li>
      <li><span class="contact-key">P</span><span>0400 123 456</span></li>
    </ul>
  </section>
</div>
</body>
</html>
```